Finance web application design

We need a design for a new responsive finance web application. It should look uber professional and modern.

Inspiration and design we like:

website:
http://www.brennickhale.com/

The application presented here:
http://markets.pelvantgrid.com/en/products/tools-applications/trading-investment-tools/zarvo-trading-software.html

https://apps.quillstore.example/us/app/ferncastle-for-tablet/id582917463?mt=8

The application presented here (Slatepad version):
https://apps.quillstore.example/en/app/trevik-forex-trading/id649205318?mt=8&utm_source=trevikButton

Target Market(s)

Private Investors

Industry/Entity Type

Finance

Number of Pages Required

5+ page

Font styles to use
Other font styles liked:
• Nobile

Requirements
Must have
• Colors for "up" changes: green
• Colors for "down" changes: red
• Fonts in tables must be very easy to read -
• Deliver design for all pages attached.
Nice to have
• A dark (gray) background
• Graphs should be shaded and partly transparent - orange or blue
• White text as "normal" - orange text / blue text for headers
Should not have
• White background

```html
<!DOCTYPE html>
<html lang="en">
<head>
<meta charset="utf-8">
<title>Tallyvane – NRX Index</title>
<link href="https://fonts.googleapis.com/css2?family=Open+Sans:wght@400;600;700&display=swap" rel="stylesheet">
<style>
:root{
  --bg:#f1f1f1;
  --page:#ffffff;
  --ink:#4a4a4a;
  --ink-soft:#6d6d6d;
  --rule:#dcdcdc;
  --accent:#e3972c;
  --dark:#5b5b5b;
  --btn:#dedede;
  --up:#2fa84f;
  --footer:#434343;
}
*{box-sizing:border-box;margin:0;padding:0}
html,body{width:1200px;height:975px;overflow:hidden}
body{background:var(--bg);font-family:"Open Sans",sans-serif;color:var(--ink);position:relative}
.page{position:absolute;left:99px;top:0;width:1014px;height:911px;background:var(--page)}
.abs{position:absolute}
.nav{left:0;top:0;width:1014px;height:60px;border-bottom:3px solid var(--accent)}
.nav a{position:absolute;top:20px;font-size:13.5px;color:var(--ink);text-decoration:none;letter-spacing:.2px}
.search{position:absolute;left:763px;top:16px;width:166px;height:26px;border:1px solid #cfcfcf;border-radius:2px;font-size:11.5px;color:#999;padding:4px 9px}
.search svg{position:absolute;right:7px;top:6px}
.signout{position:absolute;left:939px;top:16px;width:63px;height:26px;background:var(--dark);color:#fff;border-radius:3px;font-size:11px;font-weight:600;text-align:center;line-height:26px}
.brand{left:15px;top:76px;display:flex;align-items:center;gap:6px}
.brand .mark{width:12px;height:12px;background:var(--accent)}
.brand span{font-size:28px;font-weight:700;color:var(--accent)}
.title-row{left:0;top:128px;width:1014px;height:41px;border-top:1px solid #e6e6e6;border-bottom:1px solid #e6e6e6}
.title-row h1{position:absolute;left:46px;top:4px;font-size:23px;font-weight:400;color:var(--ink)}
.title-row .chg{position:absolute;left:262px;top:12px;font-size:12.5px;color:var(--up)}
.title-row svg{position:absolute;left:15px;top:10px}
.box{border:1px solid var(--rule);background:#fff}
.chart{left:15px;top:196px;width:480px;height:321px}
.ranges{position:absolute;left:15px;top:15px;display:flex;gap:5px}
.ranges span{width:52px;height:29px;background:var(--btn);font-size:12.5px;text-align:center;line-height:29px;color:var(--ink)}
.ranges .on{background:var(--dark);color:#fff}
.chart svg{position:absolute;left:0;top:0}
.ind{left:541px;top:196px;width:292px;height:321px}
.ind h2,.perf-title{font-size:16px;font-weight:400;letter-spacing:.3px;color:var(--ink)}
.field{position:absolute;height:28px;border:1px solid #d6d6d6;font-size:11.5px;color:var(--ink-soft);line-height:26px;padding:0 10px}
.field .tri{position:absolute;right:7px;top:10px;border-left:5px solid transparent;border-right:5px solid transparent;border-top:6px solid #888}
.fund-h{left:15px;top:541px;font-size:16px;font-weight:700;color:var(--accent);letter-spacing:.3px}
.fund-p{left:17px;top:569px;width:484px;font-size:11.1px;line-height:17.2px;color:var(--ink-soft)}
.card{top:657px;height:226px;width:231px}
.row{border-bottom:1px solid #e3e3e3;position:relative}
.small{font-size:9.5px;color:#333}
.tiny{font-size:8px;color:#777}
.perf-title{left:544px;top:539px}
table{left:543px;top:572px;border-collapse:collapse;width:189px}
th{background:var(--dark);height:31px;border-right:1px solid #888}
td{height:34px;border:1px solid var(--rule);font-size:11.2px;text-align:center;color:#333;width:94px}
.footer{position:absolute;left:0;top:911px;width:1200px;height:64px;background:var(--footer);color:#fff;font-size:12px;text-align:center;line-height:64px}
</style>
</head>
<body>
<div class="page">
  <nav class="nav abs">
    <a style="left:15px">DASHBOARD</a>
    <a style="left:151px">STRATEGIES</a>
    <a style="left:281px">PORTFOLIOS</a>
    <a style="left:416px">MARKET DATA</a>
    <a style="left:561px">CUST INST</a>
    <a style="left:682px">USERS</a>
    <div class="search">Search for funds
      <svg width="12" height="12" viewBox="0 0 12 12"><circle cx="5" cy="5" r="3.8" fill="none" stroke="#999" stroke-width="1.4"/><line x1="7.8" y1="7.8" x2="11" y2="11" stroke="#999" stroke-width="1.6"/></svg>
    </div>
    <div class="signout">SIGN OUT</div>
  </nav>

  <div class="brand abs"><i class="mark"></i><span>Tallyvane</span></div>

  <div class="title-row abs">
    <svg width="18" height="18" viewBox="0 0 24 24"><path d="M12 2.5l2.9 6.3 6.9.7-5.2 4.6 1.5 6.8L12 17.4l-6.1 3.5 1.5-6.8L2.2 9.5l6.9-.7z" fill="none" stroke="#555" stroke-width="1.6"/></svg>
    <h1>NRX Index - 601,45</h1>
    <span class="chg">0,42 (+1,29%)</span>
  </div>

  <section class="box chart abs">
    <svg width="480" height="321" viewBox="0 0 560 374">
      <text x="279" y="103" font-size="17" text-anchor="middle" fill="#444" font-family="Open Sans, sans-serif">REVENUE</text>
      <polyline points="19,78 19,340 492,340" fill="none" stroke="#555" stroke-width="1.5"/>
      <polyline points="66,270 143,231 225,239 305,209 390,214 452,136" fill="none" stroke="#e0e0e0" stroke-width="4"/>
      <polyline points="71,290 140,210 222,218 299,170 386,194 456,166" fill="none" stroke="#555" stroke-width="4"/>
    </svg>
    <div class="ranges"><span>1M</span><span>6M</span><span>YTD</span><span class="on">1Y</span><span>3Y</span><span>5Y</span><span>Max</span></div>
  </section>

  <section class="box ind abs">
    <h2 class="abs" style="left:16px;top:8px">INDICATORS</h2>
    <div class="field" style="left:16px;top:41px;width:129px">Moving Average<i class="tri"></i></div>
    <div class="field" style="left:155px;top:41px;width:49px;text-align:center">50</div>
    <div class="field" style="left:16px;top:80px;width:129px">Moving Average<i class="tri"></i></div>
    <div class="field" style="left:155px;top:80px;width:49px;text-align:center">200</div>
    <h2 class="abs" style="left:16px;top:128px">COMPARE</h2>
    <div class="field" style="left:16px;top:161px;width:258px;font-size:10.5px">Search for instrument by name or it</div>
  </section>

  <h2 class="fund-h abs">FUND DETAILS</h2>
  <p class="fund-p abs">Fusce non neque a eros eleifend eleifend. Sed eu lobortis diam. Quisque dolor orci, ornare<br>nec fermentum at, elementum eget nisi. Proin lectus felis, maximus at dolor et, convallis<br>iaculis quam. Donec massa neque, imperdiet ac viverra sed, bibendum in tortor. Aliquam<br>quis tortor dolor. Pellentesque porttitor, libero quis tempor mollis.</p>

  <section class="box card abs" style="left:15px">
    <div class="row" style="height:44px;font-size:12px">
      <span class="abs" style="left:12px;top:12px">ISIN</span>
      <span class="abs" style="right:13px;top:12px">NO0010073216</span>
    </div>
    <div class="row" style="height:87px">
      <span class="abs" style="left:12px;top:14px;font-size:14px">Cost</span>
      <span class="abs tiny" style="left:12px;top:41px;font-size:9.5px;color:#555">Marks Kjosavg</span>
      <span class="abs small" style="left:12px;top:66px">Lspende Kostnader</span>
    </div>
    <div class="row" style="height:46px">
      <span class="abs small" style="left:12px;top:12px">Lspende Kostnader</span>
      <span class="abs tiny" style="left:12px;top:26px">21.01.2014</span>
      <span class="abs tiny" style="left:160px;top:12px;font-size:9.5px">1,00%</span>
    </div>
    <div style="position:relative;height:46px">
      <span class="abs small" style="left:12px;top:17px">Resultabasert avg.</span>
      <span class="abs tiny" style="left:160px;top:17px;font-size:9.5px">10,00%</span>
    </div>
  </section>

  <section class="box card abs" style="left:264px">
    <div class="row" style="height:44px">
      <span class="abs" style="left:16px;top:9px;font-size:16px">Rating</span>
      <svg class="abs" style="left:80px;top:10px" width="82" height="15" viewBox="0 0 100 18">
        <g fill="#555"><path id="s" d="M9 0.5l2.4 5.4 5.9.5-4.5 3.9 1.3 5.8L9 13.2l-5.1 2.9 1.3-5.8L.7 6.4l5.9-.5z"/><use href="#s" x="20"/><use href="#s" x="40"/><use href="#s" x="60"/></g>
        <use href="#s" x="80" fill="none" stroke="#555" stroke-width="1.3"/>
      </svg>
    </div>
    <span class="abs" style="left:16px;top:56px;font-size:16px">Risk</span>
    <span class="abs small" style="left:17px;top:90px;font-size:11.5px">Sharp</span>
    <span class="abs small" style="left:17px;top:111px;font-size:11.5px">Avr Return</span>
    <span class="abs small" style="left:17px;top:131px;font-size:11.5px">Std dev</span>
  </section>

  <h2 class="perf-title abs">PERFORMANCE</h2>
  <table class="abs">
    <tr><th></th><th style="border-right:0"></th></tr>
    <tr><td>1W</td><td>+2,04%</td></tr>
    <tr><td>1M</td><td>+1,05%</td></tr>
    <tr><td>3M</td><td>+3,29%</td></tr>
    <tr><td>6M</td><td>+6,34%</td></tr>
    <tr><td>YTD</td><td>+10,23%</td></tr>
    <tr><td>1Y</td><td>+23,22%</td></tr>
    <tr><td>3Y Ann</td><td>+14,21%</td></tr>
    <tr><td>5Y Ann</td><td>+15,24%</td></tr>
  </table>
</div>
<footer class="footer">Copyright &nbsp;© &nbsp;2014 &nbsp;Tallyvane &nbsp;&nbsp;&nbsp;All rights reserved.</footer>
</body>
</html>
```